Realtor/Real Estate Investor Business Card Design

We need a business card design for a new real estate company in Maryland. We buy houses, fix and sell. We do wholesaling as well. We also rent houses.We would like to have blue background and white font.
Updates

Hi All,
I thank all of you for your efforts. You are all experts in designing.
Looking forward to meeting you online in the near future.
mira

Industry/Entity Type

Real Estate

Contact Information for Business Card

Mira Talvek
Real Estate Professional
mira@brightlanehomes.example
301-555-0148
Bright Lane Homes.com

Requirements
Must have
• House picture, and logo at the back of the card
We simplify your buying and selling real estate. at the back of the card

```html
<!DOCTYPE html>
<html lang="en">
<head>
<meta charset="utf-8">
<title>Bright Lane Homes – Business Card Back</title>
<link rel="stylesheet" href="https://fonts.googleapis.com/css2?family=Cinzel:wght@700&family=Arimo:wght@400&display=swap">
<style>
  :root {
    --band-blue: #17489b;
    --deep-blue: #1b4c9f;
    --mid-blue: #5d6db3;
    --soft-blue: #6a77ba;
    --house-blue: #1d4ea0;
    --ring-tint: rgba(200, 206, 236, 0.45);
    --wordmark: #bcc1e2;
    --text-white: #ffffff;
  }
  html, body {
    margin: 0;
    padding: 0;
    width: 1200px;
    height: 703px;
    overflow: hidden;
    background: #ffffff;
  }
  .card {
    position: relative;
    width: 1200px;
    height: 703px;
    overflow: hidden;
    background: linear-gradient(90deg, var(--deep-blue) 0%, var(--mid-blue) 35%, var(--soft-blue) 62%, var(--mid-blue) 100%);
  }
  .card__band {
    position: absolute;
    left: 0;
    top: 0;
    width: 1200px;
    height: 246px;
    background: var(--band-blue);
  }
  .card__rings {
    position: absolute;
    inset: 0;
  }
  .house-art {
    position: absolute;
    left: 56px;
    top: 264px;
    width: 785px;
    height: 140px;
    border-radius: 6px;
    background: linear-gradient(90deg, var(--house-blue) 0%, #24539f 60%, #2a57a3 100%);
  }
  .wordmark {
    position: absolute;
    left: 86px;
    top: 190px;
    margin: 0;
    font-family: "Cinzel", "Times New Roman", serif;
    font-weight: 700;
    font-size: 66px;
    line-height: 1;
    letter-spacing: 1px;
    color: var(--wordmark);
    white-space: nowrap;
  }
  .tagline {
    position: absolute;
    left: 68px;
    top: 470px;
    margin: 0;
    font-family: "Arimo", Arial, sans-serif;
    font-weight: 400;
    font-size: 50px;
    line-height: 61px;
    color: var(--text-white);
    text-transform: uppercase;
    white-space: nowrap;
  }
</style>
</head>
<body>
  <main class="card">
    <div class="card__band"></div>
    <svg class="card__rings" width="1200" height="703" viewBox="0 0 1200 703" aria-hidden="true">
      <defs>
        <clipPath id="edgeClip">
          <rect x="0" y="0" width="80" height="246"/>
        </clipPath>
      </defs>
      <circle cx="260" cy="-134" r="262" fill="none" stroke="var(--ring-tint)" stroke-width="33"/>
      <circle cx="330" cy="330" r="340" fill="none" stroke="var(--ring-tint)" stroke-width="33" clip-path="url(#edgeClip)"/>
      <circle cx="1150" cy="437" r="282" fill="none" stroke="var(--ring-tint)" stroke-width="38"/>
    </svg>
    <div class="house-art" role="img" aria-label="Illustration of a house roofline"></div>
    <h1 class="wordmark">BRIGHT LANE HOMES</h1>
    <p class="tagline">We simpify<br>your buying and<br>selling real estate</p>
  </main>
</body>
</html>
```